Junk Removal - Customers that are moving

junk collection business we want to gear this mailing to people who are moving and may need help in cleaning out the house for the open house or when the final move is near. Want to sound helpful and show it easier for us to do all the work

Target Market(s)

People Moving

Industry/Entity Type

House

Colors
3277b5
33a6d7

Requirements
Must have
• See attachment

```html
<!DOCTYPE html>
<html lang="en">
<head>
<meta charset="utf-8">
<title>1-800-HAULWELL Moving Postcard</title>
<link rel="stylesheet" href="https://fonts.googleapis.com/css2?family=Kanit:ital,wght@0,300;0,400;0,500;0,600;1,400&display=swap">
<style>
  :root {
    --brand-blue: #3277b5;
    --brand-teal: #33a6d7;
    --ink-navy: #1f4f8f;
    --ink-grey: #5d6166;
    --panel-grey: #efefef;
    --card-white: #ffffff;
    --backdrop: #e6e7e9;
  }
  * { box-sizing: border-box; margin: 0; padding: 0; }
  html, body { width: 1200px; height: 800px; overflow: hidden; }
  body {
    background: var(--backdrop);
    font-family: "Kanit", sans-serif;
    position: relative;
  }
  .postcard {
    position: absolute;
    top: 210px;
    width: 570px;
    height: 380px;
    background: var(--card-white);
    box-shadow: 0 2px 8px rgba(0,0,0,.12);
    overflow: hidden;
  }
  .postcard--back { left: 20px; }
  .postcard--front { left: 610px; }
  .corner-wedges { position: absolute; inset: 0; width: 570px; height: 380px; }

  .brand-name {
    position: absolute;
    font-weight: 600;
    color: var(--brand-blue);
    letter-spacing: -0.5px;
    line-height: 1;
  }
  .postcard--front .brand-name { top: 40px; left: 120px; font-size: 36px; }
  .mascot-area {
    position: absolute;
    top: 14px; left: 418px;
    width: 56px; height: 76px;
    border-radius: 6px;
    background: linear-gradient(180deg, #8fb3d6, #c9ccd1);
  }
  .rule {
    position: absolute;
    height: 1px;
    background: var(--brand-teal);
  }

  .greeting {
    position: absolute;
    top: 94px; left: 0; right: 0;
    text-align: center;
    line-height: 1.02;
  }
  .greeting__salutation { font-size: 23px; font-weight: 600; color: var(--ink-navy); padding-left: 40px; }
  .greeting__headline { font-size: 24px; font-weight: 400; color: var(--brand-teal); padding-left: 40px; }

  .benefits {
    position: absolute;
    top: 158px; left: 0;
    width: 375px; height: 152px;
    background: var(--panel-grey);
    padding: 7px 10px 0 12px;
  }
  .benefits__intro { font-size: 10.5px; color: var(--brand-teal); line-height: 1.2; }
  .benefits__list { list-style: none; margin-top: 4px; }
  .benefits__list li {
    font-size: 8.2px; font-weight: 300; color: var(--ink-grey); line-height: 1.22;
    padding-left: 7px; position: relative;
  }
  .benefits__list li::before { content: "•"; position: absolute; left: 0; }

  .callout {
    position: absolute;
    top: 176px; left: 386px;
    width: 184px; height: 146px;
    background: var(--brand-teal);
    color: var(--card-white);
    font-style: italic;
    font-size: 15px;
    line-height: 1.1;
    text-transform: uppercase;
    padding: 24px 10px 0 12px;
  }

  .postcard--back .brand-name { top: 34px; left: 118px; font-size: 36px; }
  .signoff {
    position: absolute;
    top: 172px; left: 30px;
    width: 240px;
    font-size: 13px;
    line-height: 1.12;
    color: #222;
  }
  .signoff__wish { font-style: italic; margin-top: 10px; }
  .signoff__team { margin-top: 8px; }
  .address-divider {
    position: absolute;
    left: 285px; top: 150px;
    width: 3px; height: 200px;
    background: var(--brand-teal);
  }
</style>
</head>
<body>

  <section class="postcard postcard--back" aria-label="Postcard back">
    <svg class="corner-wedges" viewBox="0 0 570 380" aria-hidden="true">
      <polygon points="0,0 118,0 118,24 0,8" fill="var(--brand-teal)"/>
    </svg>
    <div class="brand-name">1-800-HAULWELL</div>
    <div class="rule" style="top:84px;left:0;width:570px;"></div>
    <div class="signoff">
      <p>Visit our website:<br>www.haulwellhome.com<br>or give us a call for more information.</p>
      <p class="signoff__wish">Wishing you the best of luck<br>in your new home!</p>
      <p class="signoff__team">The 1-800 HAULWELL Team</p>
    </div>
    <div class="address-divider"></div>
  </section>

  <section class="postcard postcard--front" aria-label="Postcard front">
    <svg class="corner-wedges" viewBox="0 0 570 380" aria-hidden="true">
      <polygon points="0,0 125,0 125,28 0,6" fill="var(--brand-teal)"/>
      <polygon points="445,24 570,6 570,24" fill="var(--brand-teal)"/>
    </svg>
    <div class="brand-name">1-800-HAULWELL</div>
    <div class="mascot-area" role="img" aria-label="Cartoon junk-removal worker leaning on a broom beside a trash can"></div>
    <div class="rule" style="top:62px;left:0;width:115px;"></div>
    <div class="rule" style="top:90px;left:470px;width:100px;"></div>

    <div class="greeting">
      <h1 class="greeting__salutation">Dear Homeowner,</h1>
      <h2 class="greeting__headline">Congratulations on your upcoming move!</h2>
    </div>

    <div class="benefits">
      <p class="benefits__intro">We know how exciting and stressful moving your family and all your belongings can be.<br>Let 1-800-HAULWELL help you! Here's how:</p>
      <ul class="benefits__list">
        <li>No need to collect and remove unwanted items from the property; just point it out and we do all the work!</li>
        <li>No storage units or dumpsters to deal with, no physical work to worry about</li>
        <li>We leave the areas from which we remove your unwanted "junk" "broom clean"</li>
        <li>Our up front price is not an estimate; the price we quote is the price you pay!</li>
        <li>We responsibly dispose of or recycle all items we remove</li>
        <li>We are fully licensed (DEP #0051290) and insured</li>
        <li>More than 75 years of family business behind all our work</li>
        <li>Our services are ideal for both the initial cleanout of your for your open house or final cleanout days before moving 1-800HAULWELL (1-800-555-0199) is the one number to call.</li>
      </ul>
    </div>

    <div class="callout">Let 1-800-Haul-Well help take some of the stress out of your move!</div>
  </section>

</body>
</html>
```